Business Card - Cooperate

Business Card for Larkfield Management Consulting

Target Market(s)

Corparte - b2B

Industry/Entity Type

Management Consulting - Professional Services

Contact Information for Business Card

Company Name , Slogan , Dummy Address,

Requirements
Must have
• Reach your Full Potential

```html
<!DOCTYPE html>
<html lang="en">
<head>
<meta charset="utf-8">
<title>Larkfield Management Consulting – Business Card</title>
<link rel="stylesheet" href="https://fonts.googleapis.com/css2?family=Rubik:wght@400;500;600;700&display=swap">
<style>
  :root {
    --page-bg: #e9e9e9;
    --card-bg: #f7f7f5;
    --brand-blue: #27409a;
    --brand-navy: #24246b;
    --brand-green: #4cb748;
    --brand-teal: #1ea48c;
    --ink: #1d1d1f;
    --card-shadow: 0 18px 40px rgba(0, 0, 0, 0.16), 0 3px 8px rgba(0, 0, 0, 0.08);
  }
  * { box-sizing: border-box; margin: 0; padding: 0; }
  html, body {
    width: 1200px;
    height: 900px;
    overflow: hidden;
    background: var(--page-bg);
    font-family: "Rubik", Arial, sans-serif;
    color: var(--ink);
  }
  .canvas {
    position: relative;
    width: 1200px;
    height: 900px;
  }
  .card {
    position: absolute;
    left: 348px;
    width: 504px;
    height: 288px;
    background: var(--card-bg);
    box-shadow: var(--card-shadow);
    overflow: hidden;
  }
  .card--front { top: 110px; }
  .card--back { top: 480px; }

  /* Front side */
  .brand-block {
    position: absolute;
    left: 120px;
    top: 78px;
    display: flex;
    flex-direction: column;
  }
  .brand-lockup {
    display: flex;
    align-items: center;
    gap: 14px;
  }
  .brand-dot {
    width: 38px;
    height: 38px;
    border-radius: 50%;
    background: var(--brand-blue);
  }
  .brand-name {
    font-size: 50px;
    font-weight: 500;
    color: var(--brand-blue);
    letter-spacing: 1px;
    line-height: 1;
  }
  .brand-tagline {
    margin-top: 10px;
    margin-left: 52px;
    font-size: 11px;
    font-weight: 600;
    letter-spacing: 3.2px;
    color: var(--brand-teal);
    text-transform: uppercase;
  }
  .front-address {
    position: absolute;
    left: 120px;
    top: 200px;
    font-size: 12px;
    letter-spacing: 0.3px;
  }

  /* Back side */
  .name-band {
    position: absolute;
    inset: 0;
    width: 504px;
    height: 288px;
  }
  .person {
    position: absolute;
    left: 34px;
    top: 24px;
    color: #fff;
  }
  .person-name {
    font-size: 17px;
    font-weight: 600;
    letter-spacing: 1.5px;
    text-transform: uppercase;
  }
  .person-role {
    font-size: 12px;
    font-weight: 400;
    margin-top: 2px;
  }
  .contact-list {
    position: absolute;
    left: 34px;
    top: 142px;
    list-style: none;
    font-size: 12px;
    line-height: 19px;
  }
  .contact-list li {
    display: flex;
    align-items: center;
    gap: 8px;
  }
  .contact-icon {
    width: 11px;
    height: 11px;
    fill: var(--brand-blue);
    flex: none;
  }
  .back-tagline {
    position: absolute;
    left: 34px;
    top: 222px;
    font-size: 13px;
    font-weight: 700;
  }
  .back-brand {
    position: absolute;
    right: 36px;
    bottom: 40px;
    display: flex;
    align-items: center;
    gap: 10px;
  }
  .back-brand .brand-dot {
    width: 26px;
    height: 26px;
  }
  .back-brand .brand-name {
    font-size: 30px;
  }
</style>
</head>
<body>
<main class="canvas">

  <section class="card card--front" aria-label="Business card front">
    <div class="brand-block">
      <div class="brand-lockup">
        <span class="brand-dot"></span>
        <span class="brand-name">larkfield</span>
      </div>
      <p class="brand-tagline">Reach your full potential</p>
    </div>
    <p class="front-address">Street Name,&nbsp; Zip Code 12345, City Name</p>
  </section>

  <section class="card card--back" aria-label="Business card back">
    <svg class="name-band" viewBox="0 0 504 288" aria-hidden="true">
      <path d="M0 0 H318 A420 420 0 0 1 0 96 Z" fill="#ffffff"/>
      <path d="M0 0 H300 A400 400 0 0 1 0 86 Z" fill="var(--brand-blue)"/>
      <path d="M318 0 A420 420 0 0 1 0 96" fill="none" stroke="var(--brand-green)" stroke-width="2.5"/>
    </svg>

    <div class="person">
      <p class="person-name">Marcus Hale</p>
      <p class="person-role">Director</p>
    </div>

    <ul class="contact-list">
      <li>
        <svg class="contact-icon" viewBox="0 0 24 24"><path d="M6.6 10.8a15.1 15.1 0 0 0 6.6 6.6l2.2-2.2a1 1 0 0 1 1-.25 11.4 11.4 0 0 0 3.6.57 1 1 0 0 1 1 1V20a1 1 0 0 1-1 1A17 17 0 0 1 3 4a1 1 0 0 1 1-1h3.5a1 1 0 0 1 1 1c0 1.25.2 2.45.57 3.57a1 1 0 0 1-.25 1z"/></svg>
        <span>555 018 4472</span>
      </li>
      <li>
        <svg class="contact-icon" viewBox="0 0 24 24"><path d="M2 5h20v14H2z M2 5l10 8 10-8" fill="var(--brand-blue)" stroke="#fff" stroke-width="1.5"/></svg>
        <span>hello@larkfieldmail.com</span>
      </li>
      <li>
        <svg class="contact-icon" viewBox="0 0 24 24"><circle cx="12" cy="12" r="10" fill="none" stroke="var(--brand-blue)" stroke-width="2"/><path d="M2 12h20M12 2c3 3 3 17 0 20M12 2c-3 3-3 17 0 20" fill="none" stroke="var(--brand-blue)" stroke-width="1.8"/></svg>
        <span>www.larkfieldweb.com</span>
      </li>
    </ul>

    <p class="back-tagline">reach your full potential</p>

    <div class="back-brand">
      <span class="brand-dot"></span>
      <span class="brand-name">larkfield</span>
    </div>
  </section>

</main>
</body>
</html>
```